■デザインへの要望
1)フライヤーのイメージとしては明るく女性的なイメージを希望します。
2)人物写真は使わないでください。
3)コーポレートロゴを右上に配置してください。
ロゴの改変(色の変更や比率の変更)はご遠慮ください。
4)会のロゴを配置してください。
位置はお任せしますが、サイズの変更はご遠慮ください。
※前回のフライヤーを素材と一緒にお付けしますのでご参考になさってください。

■素材
1)フライヤーを作成する際に必要なロゴ等の画像等は

```html
<!DOCTYPE html>
<html lang="ja">
<head>
<meta charset="utf-8">
<title>ランチョンセミナー15</title>
<link href="https://fonts.googleapis.com/css2?family=Noto+Sans+JP:wght@400;500;700;900&family=Noto+Serif+JP:wght@500;700&family=Noto+Serif:wght@400&display=swap" rel="stylesheet">
<style>
  :root{
    --navy:#1b3f87;
    --blue:#2f6fc0;
    --sky:#5aa6dc;
    --tag-bg:#d7ecf8;
    --ink:#333a45;
    --grey:#8b8f96;
    --pill:#2d63b4;
    --line:#cfd6df;
    --green:#5a9e3c;
  }
  *{margin:0;padding:0;box-sizing:border-box}
  html,body{width:849px;height:1200px;overflow:hidden;background:#fff}
  body{font-family:"Noto Sans JP",sans-serif;color:var(--ink)}
  .flyer{position:relative;width:849px;height:1200px;overflow:hidden;
    background:
      radial-gradient(circle at 92% 58%, rgba(255,214,120,.55) 0 9%, transparent 22%),
      radial-gradient(circle at 8% 55%, rgba(255,182,210,.45) 0 8%, transparent 24%),
      radial-gradient(circle at 85% 30%, rgba(160,220,250,.55) 0 10%, transparent 26%),
      radial-gradient(circle at 15% 25%, rgba(200,235,180,.45) 0 8%, transparent 24%),
      radial-gradient(circle at 70% 80%, rgba(210,190,250,.35) 0 10%, transparent 28%),
      #fff;}
  .society{position:absolute;left:56px;top:30px;display:flex;align-items:center;gap:12px}
  .society-mark{width:46px;height:46px;border-radius:50%;background:var(--blue)}
  .society-name{font-weight:700;font-size:20px;color:var(--blue)}
  .congress{position:absolute;left:56px;top:116px;font-size:24px;font-weight:700;color:var(--navy)}
  .sponsor-brand{position:absolute;right:50px;top:36px;display:flex;align-items:center;gap:10px}
  .sponsor-brand .dot{width:30px;height:30px;border-radius:50%;background:var(--green)}
  .sponsor-brand span{font-size:26px;font-weight:700;color:var(--green)}
  .seminar-tag{position:absolute;left:56px;top:164px;padding:4px 22px;background:var(--tag-bg);border-radius:6px;
    font-size:26px;font-weight:700;color:var(--blue)}
  .title{position:absolute;left:0;right:0;top:222px;text-align:center;font-family:"Noto Serif JP",serif;font-weight:700;
    font-size:66px;line-height:88px;color:var(--navy);letter-spacing:2px}
  .subtitle{position:absolute;left:0;right:0;top:472px;text-align:center;font-family:"Noto Serif JP",serif;font-weight:500;
    font-size:30px;color:var(--sky)}
  .english{position:absolute;left:0;right:0;top:522px;text-align:center;font-family:"Noto Serif",serif;font-size:28px;color:var(--blue)}
  .info{position:absolute;left:150px;display:flex;align-items:center;gap:20px;color:var(--navy)}
  .pill{display:inline-block;width:78px;padding:4px 0;text-align:center;border-radius:20px;background:var(--pill);color:#fff;font-size:22px;font-weight:700}
  .date{top:618px;font-size:34px;font-weight:700}
  .date .big{font-size:42px}
  .venue{top:690px}
  .venue .room{font-size:36px;font-weight:700}
  .venue .place{font-size:20px;font-weight:500;line-height:1.35}
  .people{position:absolute;left:70px;right:70px;top:800px;border-top:2px solid var(--line)}
  .row{display:flex;border-bottom:2px solid var(--line);padding:16px 0}
  .role{width:140px;display:flex;align-items:flex-start;justify-content:center;padding-top:6px}
  .role span{background:#6d7580;color:#fff;font-size:20px;font-weight:700;padding:4px 18px;border-radius:4px;letter-spacing:6px}
  .who{flex:1;padding-left:34px}
  .name{font-family:"Noto Serif JP",serif;font-size:38px;font-weight:700;color:var(--navy)}
  .name small{font-size:22px;margin-left:10px}
  .aff{font-size:15px;color:var(--ink);line-height:1.6;margin-top:2px}
  .footer{position:absolute;left:56px;bottom:26px;font-size:17px;color:var(--ink)}
</style>
</head>
<body>
<div class="flyer">
  <div class="society"><div class="society-mark"></div><div class="society-name">SNCA</div></div>
  <div class="sponsor-brand"><div class="dot"></div><span>ミモザ</span></div>
  <div class="congress">第25回 日本えんげケア看護学会学術大会</div>
  <div class="seminar-tag">ランチョンセミナー15</div>

  <h1 class="title">これからの<br>摂食嚥下障害看護に<br>何が求められているか</h1>
  <p class="subtitle">～「機能低下予防」と「終末期care」～</p>
  <p class="english">What is required in the future for dysphagia nursing</p>

  <div class="info date"><span class="pill">日時</span><span>2019年 <span class="big">9</span>月 <span class="big">7</span>日(土) 12:00～13:00</span></div>
  <div class="info venue"><span class="pill">会場</span><span class="room">第8会場</span><span class="place">みなと国際会議センター<br>2F 中会議室201</span></div>

  <div class="people">
    <div class="row">
      <div class="role"><span>座長</span></div>
      <div class="who"><div class="name">青山 春香<small>先生</small></div><div class="aff">緑丘看護大学 名誉教授</div></div>
    </div>
    <div class="row">
      <div class="role"><span>演者</span></div>
      <div class="who"><div class="name">森下 千尋<small>先生</small></div>
        <div class="aff">一般社団法人東山看護協会 認定看護師教育課程専任教員<br>摂食・嚥下障害看護認定看護師 主任教員</div></div>
    </div>
  </div>

  <div class="footer">［共 催］ 第25回日本えんげケア看護学会学術大会　ミモザ株式会社</div>
</div>
</body>
</html>
```